KAVELUXE Consultancy Business Card

We need a business card design for a new Image & Etiquette Consultancy Company.

The design should reflect the corporate colour found in the logo attached.

Info to include:

Name: Marelda Quon
Title: Image Consultant
Company: KA VELUXE CONSULTANCY
Address: 27 Pelham Street, #14-08 Harbourview Tower, Singapore 048215
Contact: 9317 6408
Email: marelda@kaveluxe.com.sg
Website: www.kaveluxe.com.sg

Industry/Entity Type

Business

```html
<!DOCTYPE html>
<html lang="en">
<head>
<meta charset="utf-8">
<title>KA VELUXE Consultancy – Business Card</title>
<link rel="stylesheet" href="https://fonts.googleapis.com/css2?family=Open+Sans:wght@400;600&display=swap">
<style>
  :root {
    --plum: #3a1551;
    --gold: #e5b41e;
    --gold-deep: #d9a417;
    --gold-light: #f7e27a;
    --ink: #2e2e2e;
    --paper: #ffffff;
    --backdrop: #e9e4dc;
  }
  * { margin: 0; padding: 0; box-sizing: border-box; }
  html, body { width: 1200px; height: 1081px; overflow: hidden; }
  body {
    position: relative;
    background: var(--backdrop);
    font-family: "Open Sans", Arial, sans-serif;
    color: var(--ink);
  }
  .card { position: absolute; overflow: hidden; box-shadow: 0 4px 14px rgba(0,0,0,.25); }

  /* Front */
  .card-front { left: 38px; top: 38px; width: 821px; height: 472px; background: var(--paper); }
  .brand { position: absolute; left: 0; right: 0; text-align: center; }
  .brand-name {
    font-weight: 400; color: var(--plum); letter-spacing: 3px; line-height: 1;
  }
  .brand-tagline {
    font-weight: 600; color: var(--gold-deep); letter-spacing: 1px; margin-top: 8px;
  }
  .card-front .brand { top: 98px; padding-right: 30px; }
  .card-front .brand-name { font-size: 66px; }
  .card-front .brand-tagline { font-size: 19px; }

  .address {
    position: absolute; right: 449px; top: 256px; text-align: right;
    font-size: 17px; line-height: 36px; font-style: normal;
  }
  .divider { position: absolute; left: 391px; top: 258px; width: 1px; height: 108px; background: #9a9a9a; }
  .contacts { position: absolute; left: 406px; top: 256px; list-style: none; font-size: 17px; line-height: 36px; }
  .contacts li { display: flex; align-items: center; gap: 8px; }
  .contacts svg { width: 17px; height: 17px; flex: none; }

  .footer-band { position: absolute; left: 0; bottom: 0; width: 821px; height: 60px; }
  .holder {
    position: absolute; right: 26px; bottom: 14px; color: var(--paper);
    font-size: 23px; font-weight: 600; white-space: nowrap;
  }
  .holder .role { font-size: 19px; font-weight: 400; }

  /* Back */
  .card-back {
    left: 338px; top: 560px; width: 825px; height: 470px;
    background: radial-gradient(ellipse at 45% 40%, var(--gold-light) 0%, var(--gold) 65%, var(--gold-deep) 100%);
  }
  .card-back .brand { top: 180px; padding-left: 16px; }
  .card-back .brand-name { font-size: 68px; }
  .card-back .brand-tagline { font-size: 20px; color: var(--plum); }
  .website-large {
    position: absolute; left: 0; right: 0; top: 337px; text-align: center;
    font-size: 23px; letter-spacing: 2.5px; color: var(--ink);
  }
</style>
</head>
<body>

<section class="card card-front" aria-label="Business card front">
  <div class="brand">
    <div class="brand-name">KA VELUXE</div>
    <div class="brand-tagline">CONSULTANCY · Carry Yourself Well</div>
  </div>

  <address class="address">
    27 Pelham Street<br>
    #14-08 Harbourview Tower<br>
    Singapore 048215
  </address>
  <div class="divider"></div>
  <ul class="contacts">
    <li>
      <svg viewBox="0 0 20 20" aria-hidden="true"><circle cx="10" cy="10" r="10" fill="var(--gold)"/><path d="M7 5.5h2l1 3-1.4 1a6 6 0 0 0 2.9 2.9l1-1.4 3 1v2c0 .6-.5 1-1 1A9 9 0 0 1 6 6.5c0-.5.4-1 1-1z" fill="#fff"/></svg>
      9317 6408
    </li>
    <li>
      <svg viewBox="0 0 20 20" aria-hidden="true"><circle cx="10" cy="10" r="10" fill="var(--gold)"/><rect x="5" y="6.5" width="10" height="7" fill="#fff"/><path d="M5 6.5l5 4 5-4" fill="none" stroke="var(--gold)" stroke-width="1.2"/></svg>
      marelda@kaveluxe.com.sg
    </li>
    <li>
      <svg viewBox="0 0 20 20" aria-hidden="true"><circle cx="10" cy="10" r="10" fill="var(--gold)"/><circle cx="10" cy="10" r="5" fill="none" stroke="#fff" stroke-width="1.3"/><path d="M5 10h10M10 5c-2.5 3-2.5 7 0 10M10 5c2.5 3 2.5 7 0 10" fill="none" stroke="#fff" stroke-width="1"/></svg>
      www.kaveluxe.com.sg
    </li>
  </ul>

  <svg class="footer-band" viewBox="0 0 821 60" preserveAspectRatio="none" aria-hidden="true">
    <rect x="0" y="18" width="440" height="15" fill="var(--gold)"/>
    <path d="M0 33 H395 C415 33 420 4 460 2 H821 V60 H0 Z" fill="var(--plum)"/>
  </svg>
  <div class="holder">Marelda Quon, <span class="role">Image Consultant</span></div>
</section>

<section class="card card-back" aria-label="Business card back">
  <div class="brand">
    <div class="brand-name">KA VELUXE</div>
    <div class="brand-tagline">CONSULTANCY · Carry Yourself Well</div>
  </div>
  <div class="website-large">www.kaveluxe.com.sg</div>
</section>

</body>
</html>
```